Ophthalmic device company needs packaging modernization

We are medical device company that needs a new look for their packaging design. It should look clean and sophisticated. The logo must not be changed. Please maintain the branding of the logo.

Refer to the attached product brochure for the product specifications and the packaging template we want designed.

The box design should fit within our branding style which you can view at www.pemarix.com

Please message me if anything is unclear.

Target Market(s)

Eye Surgeons, eye surgery patients

Industry/Entity Type

It Company

```html
<!DOCTYPE html>
<html lang="en">
<head>
<meta charset="utf-8">
<title>Pemarix PX Aspheric – Lens Box Panels</title>
<link href="https://fonts.googleapis.com/css2?family=Montserrat:wght@400;500;600;700&display=swap" rel="stylesheet">
<style>
  :root {
    --stage: #aab3b7;
    --paper: #f2f3f4;
    --magenta: #b0194f;
    --magenta-deep: #9a1444;
    --rose: rgba(255, 190, 210, 0.45);
    --ink: #2f2f33;
    --white: #ffffff;
  }
  * { box-sizing: border-box; margin: 0; padding: 0; }
  html, body { width: 1200px; height: 918px; overflow: hidden; }
  body {
    background: var(--stage);
    font-family: "Montserrat", sans-serif;
    position: relative;
  }
  .panel {
    position: absolute;
    top: 110px;
    width: 400px;
    height: 700px;
    background: var(--magenta);
    overflow: hidden;
  }
  .panel--front { left: 150px; }
  .panel--back { left: 650px; }

  .panel__cap {
    height: 150px;
    background: var(--paper);
    position: relative;
  }
  .brand {
    position: absolute;
    display: flex;
    align-items: center;
    gap: 8px;
    color: var(--ink);
    font-weight: 600;
    letter-spacing: 1px;
  }
  .brand__dot {
    width: 14px; height: 14px; border-radius: 50%;
    background: var(--magenta);
  }
  .panel--front .brand { left: 36px; top: 54px; font-size: 40px; }
  .panel--back .brand { left: 30px; top: 60px; font-size: 24px; }
  .panel--back .brand__dot { width: 10px; height: 10px; }

  .lens-art {
    position: absolute;
    left: 120px; top: 90px;
    width: 170px; height: 300px;
    border-radius: 85px;
    background: radial-gradient(circle at 50% 50%, #c9d0d8 0%, #dfe3e8 45%, rgba(230,233,236,0.0) 72%);
  }

  .claim-band {
    position: absolute;
    left: 40px; top: 400px;
    width: 360px; height: 80px;
    background: var(--rose);
    border-left: 5px solid rgba(255,255,255,0.5);
    padding: 10px 0 0 10px;
    color: var(--white);
    font-weight: 600;
    font-size: 22px;
    line-height: 1.1;
    text-transform: uppercase;
  }
  .product-name {
    position: absolute;
    left: 52px; top: 500px;
    display: flex; align-items: flex-end; gap: 6px;
    color: var(--ink);
    font-weight: 700;
  }
  .product-name__code { font-size: 34px; line-height: 1; }
  .product-name__type { font-size: 22px; color: var(--white); font-weight: 600; text-transform: uppercase; }
  .edge-tag {
    position: absolute;
    left: 262px; top: 494px;
    width: 138px; height: 46px;
    background: var(--rose);
    padding: 4px 0 0 6px;
    color: var(--white);
  }
  .edge-tag__num { font-size: 22px; font-weight: 700; line-height: 1; }
  .edge-tag__label { font-size: 9px; font-weight: 700; color: var(--ink); }

  .lens-type {
    position: absolute;
    left: 0; right: 0; top: 572px;
    text-align: center;
    color: var(--ink);
    font-size: 13px;
    letter-spacing: 0.5px;
  }
  .front-footer {
    position: absolute;
    left: 0; right: 0; top: 598px;
    border-top: 3px solid var(--ink);
    border-bottom: 2px solid var(--ink);
    padding: 8px 10px 6px;
    display: flex; justify-content: space-between; align-items: center;
    color: var(--white);
    font-size: 8.5px;
  }
  .front-footer__web { font-size: 11px; font-style: normal; }

  .benefits { position: absolute; left: 0; right: 0; top: 170px; }
  .benefit {
    height: 62px;
    margin-bottom: 10px;
    background: var(--rose);
    display: flex; align-items: center; justify-content: center;
    text-align: center;
    color: var(--white);
    font-size: 12px;
    padding: 0 90px;
    line-height: 1.4;
  }

  .back-base {
    position: absolute;
    left: 0; right: 0; top: 470px; bottom: 0;
    background: var(--magenta-deep);
    padding: 18px 16px;
    display: grid;
    grid-template-columns: 175px 1fr;
    gap: 16px;
    color: var(--white);
  }
  .spec-table { width: 100%; border-collapse: separate; border-spacing: 0 4px; font-size: 7.5px; }
  .spec-table td { background: var(--white); color: var(--ink); padding: 3px 5px; }
  .spec-table td:last-child { color: var(--magenta); }
  .address { font-size: 11px; line-height: 1.35; }
  .contact { margin-top: 8px; font-size: 10px; font-weight: 600; }
  .marks { display: flex; gap: 8px; margin-top: 14px; align-items: center; }
  .mark-circle { width: 26px; height: 26px; border-radius: 50%; background: var(--ink); }
  .mark-square { width: 18px; height: 18px; border: 1.5px solid var(--white); }
  .iso { font-size: 8px; line-height: 1.3; }
</style>
</head>
<body>

  <section class="panel panel--front">
    <div class="panel__cap">
      <div class="brand"><span class="brand__dot"></span>PEMARIX</div>
    </div>
    <div class="lens-art" role="img" aria-label="Illustration of a clear intraocular lens with curved haptics"></div>
    <div class="claim-band">Natural Yellow<br>Hydrophobic Acrylic</div>
    <div class="product-name">
      <span class="product-name__code">PX</span>
      <span class="product-name__type">Aspheric</span>
    </div>
    <div class="edge-tag">
      <div class="edge-tag__num">360°</div>
      <div class="edge-tag__label">Square Edge</div>
    </div>
    <p class="lens-type">FOLDABLE INTRAOCULAR LENS</p>
    <div class="front-footer">
      <span>CAUTION: Federal law restricts this device to sale by or on the order of a physician</span>
      <span class="front-footer__web">www.pemarix.com</span>
    </div>
  </section>

  <section class="panel panel--back">
    <div class="panel__cap">
      <div class="brand"><span class="brand__dot"></span>PEMARIX</div>
    </div>
    <div class="benefits">
      <p class="benefit">Offers superior optical centering properties</p>
      <p class="benefit">Unfold time less than 10 seconds</p>
      <p class="benefit">Edge profile to reduce dysphotopsia on frontside</p>
      <p class="benefit">Glistening free optics</p>
    </div>
    <div class="back-base">
      <div>
        <table class="spec-table">
          <tr><td>Optic material</td><td>Hydrophobic acrylic</td></tr>
          <tr><td>Optic style</td><td>Biconvex</td></tr>
          <tr><td>Diameter</td><td>13.0 mm</td></tr>
          <tr><td>Position holes</td><td>0</td></tr>
          <tr><td>Chamber depth</td><td>5.0 mm</td></tr>
          <tr><td>Diopter range</td><td>10.0 – 30.0 D</td></tr>
        </table>
        <div class="marks">
          <span class="mark-square"></span>
          <span class="iso">ISO 9001<br>ISO 13485</span>
        </div>
      </div>
      <div>
        <p class="address">1840 Harrow Mill Road,<br>ASHFORD, Ohio 44120</p>
        <p class="contact">info@pemarix.com</p>
        <div class="marks">
          <span class="mark-circle"></span>
          <span class="mark-square"></span>
          <span class="mark-square"></span>
        </div>
      </div>
    </div>
  </section>

</body>
</html>
```